RW Talbrook LLC Business Card - Civil Engineering & Consulting Firm

We need a Business Card that is elegant, and masculine.  It is our Professional Civil Engineering & Consulting Company located in San Antonio TX (Not s construction or builder firm- no gears & no tool images please). We provide civil engineering services including  commercial site plans, grading and drainage plans, utility plans, hydraulics and hydrology, land planning, utility coordination, and other general civil engineering services related to commercial and residential development.
We have 2 existing Logos. We would like to convey reliability, strength, trustworthiness and attention to detail.  Blues and orange tones as per logo We are OK with the use of a darker blue in the mix.  We have 2 logo versions - Full Company Name Logo to go on the back of card, & Small Icon Logo for the front w/ personal Info.

Target Market(s)
Architects, Real Estate Developers, Other Strctural Engineers, Surveyers, General Contractors
Industry/Entity Type
Professional Civil Engineering
Contact Information for Business Card
Name, Position, Address, Cell & Office #, email, and company website
Font styles to use
Other font styles liked:
- Avian
Requirements
Should not have
- No Tools, No Gears, no Cranes, or Construction Equipment.

```html
<!DOCTYPE html>
<html lang="en">
<head>
<meta charset="utf-8">
<title>RW Talbrook LLC Business Card</title>
<link rel="stylesheet" href="https://fonts.googleapis.com/css2?family=Montserrat:wght@400;500;700&display=swap">
<style>
  :root {
    --stage: #3b3b3b;
    --card: #171717;
    --sky: #7aaedb;
    --amber: #f0962a;
    --ink: #f2f2f2;
  }
  * { box-sizing: border-box; margin: 0; padding: 0; }
  html, body { width: 1200px; height: 801px; overflow: hidden; }
  body {
    background: var(--stage);
    font-family: "Montserrat", sans-serif;
    position: relative;
  }
  .card {
    position: absolute;
    top: 252px;
    width: 520px;
    height: 297px;
    background: var(--card);
    overflow: hidden;
  }
  .card-front { left: 50px; }
  .card-back { left: 630px; border-bottom: 3px solid var(--sky); }

  .front-swoosh { position: absolute; inset: 0; width: 100%; height: 100%; }

  .brand-name {
    position: absolute;
    left: 30px;
    top: 118px;
    font-size: 21px;
    font-weight: 500;
    letter-spacing: 1px;
    color: var(--sky);
  }
  .divider {
    position: absolute;
    left: 246px;
    top: 34px;
    width: 1px;
    height: 140px;
    background: var(--sky);
  }
  .contact {
    position: absolute;
    left: 262px;
    top: 30px;
    color: var(--ink);
    font-size: 11px;
    line-height: 1.45;
  }
  .contact .person-name {
    color: var(--sky);
    font-weight: 700;
    font-size: 16px;
    letter-spacing: 0.5px;
    line-height: 1.2;
  }
  .contact .role { margin-bottom: 8px; }
  .contact .address { margin-bottom: 8px; }
  .contact-line { display: flex; align-items: center; gap: 7px; }
  .contact-line svg { width: 10px; height: 10px; flex: none; }

  .back-pattern {
    position: absolute;
    inset: 0;
    background: linear-gradient(115deg, #121212 0%, #1c1c1c 55%, #262626 100%);
  }
  .back-name {
    position: absolute;
    left: 50%;
    top: 50%;
    transform: translate(-50%, -50%);
    font-size: 20px;
    font-weight: 500;
    letter-spacing: 1px;
    color: var(--amber);
    white-space: nowrap;
  }
</style>
</head>
<body>
  <section class="card card-front">
    <svg class="front-swoosh" viewBox="0 0 520 297" preserveAspectRatio="none" aria-hidden="true">
      <path d="M0 280 C 300 295, 505 260, 520 40 L 520 297 L 0 297 Z" fill="var(--sky)"/>
      <path d="M0 274 C 300 289, 500 254, 514 30" fill="none" stroke="var(--amber)" stroke-width="4"/>
    </svg>

    <div class="brand-name">RW Talbrook LLC</div>
    <div class="divider"></div>

    <div class="contact">
      <div class="person-name">DAN CORLISS</div>
      <div class="role">President</div>
      <div class="address">4180 Harbor Crest Way<br>Bayview CA 92210</div>
      <div class="contact-line">
        <svg viewBox="0 0 10 10"><rect x="2.5" y="0.5" width="5" height="9" rx="1" fill="none" stroke="var(--amber)" stroke-width="1.2"/></svg>
        555-240-6118
      </div>
      <div class="contact-line">
        <svg viewBox="0 0 10 10"><path d="M2 1 L4 3 L3 4.5 Q4.5 6.5 5.5 7 L7 6 L9 8 L7.5 9.5 Q2 8 0.5 2.5 Z" fill="var(--amber)"/></svg>
        555-240-6119
      </div>
      <div class="contact-line">
        <svg viewBox="0 0 10 10"><rect x="0.5" y="2" width="9" height="6" fill="var(--amber)"/><path d="M0.5 2 L5 5.5 L9.5 2" fill="none" stroke="var(--card)" stroke-width="0.9"/></svg>
        info@rwtalbrookconsulting.com
      </div>
      <div class="contact-line">
        <svg viewBox="0 0 10 10"><circle cx="5" cy="5" r="4.5" fill="var(--amber)"/><path d="M0.5 5 H9.5 M5 0.5 V9.5" stroke="var(--card)" stroke-width="0.8"/></svg>
        www.rwtalbrookconsulting.com
      </div>
    </div>
  </section>

  <section class="card card-back">
    <div class="back-pattern" role="img" aria-label="Tonal embossed repeating monogram pattern in dark greys"></div>
    <div class="back-name">RW Talbrook LLC</div>
  </section>
</body>
</html>
```